Business Card for staff member of football club SC Brenval

I would like to get a business card template for all staff member of our soccer club.

The card should use as much as possible the 2 colors of the club : Red which is the main color and blue which is the alternative color. It can be balanced between the two like our logo.

I prefer simple and lean design.

Contact Information for Business Card

Bussiness card should have all main stuff as describe here below in must have.

Font styles to use
Sans Serif

Requirements
Must have
• Name : Laurent DESPRATIN
Fonction : Président
Mobile : +41 xx xxx xx xx
Email : first.lastname@scbrenval.ch
Adresse of the club : SC Brenval, 1873 Brenval
Website of the club : www.scbrenval.ch
Nice to have
• Version with and without picture of the staff member

A version for men, a version for women staff member.

```html
<!DOCTYPE html>
<html lang="en">
<head>
<meta charset="utf-8">
<title>SC Brenval – Business Card</title>
<link rel="stylesheet" href="https://fonts.googleapis.com/css2?family=Roboto:wght@400;700;900&display=swap">
<style>
  :root {
    --club-red: #e8253a;
    --club-blue: #1e8fd6;
    --ink: #1b1b1b;
    --card-dark: #2a2a2a;
    --paper: #ffffff;
    --ball-grey: #6c6462;
    --backdrop: #e9e9e9;
  }
  * { margin: 0; padding: 0; box-sizing: border-box; }
  html, body { width: 1200px; height: 901px; overflow: hidden; }
  body {
    background: var(--backdrop);
    font-family: "Roboto", Arial, sans-serif;
    position: relative;
  }
  .card { position: absolute; overflow: hidden; border-radius: 3px; }

  /* Back of card */
  .card-back {
    left: 420px; top: 40px; width: 640px; height: 352px;
    background: var(--card-dark);
  }
  .card-back .club-mark {
    position: absolute; left: 180px; top: 150px;
    display: flex; align-items: center; gap: 16px;
  }
  .club-mark .mark-square { width: 44px; height: 44px; background: var(--club-red); }
  .card-back .club-name {
    color: #ffffff; font-weight: 900; font-size: 36px; letter-spacing: 0.5px;
  }

  /* Front of card */
  .card-front {
    left: 140px; top: 420px; width: 800px; height: 440px;
    background: var(--paper);
  }
  .blue-band {
    position: absolute; left: 0; top: 70px; width: 200px; height: 118px;
    background: var(--club-blue);
  }
  .red-band {
    position: absolute; left: 200px; top: 112px; width: 600px; height: 130px;
    background: var(--club-red);
  }
  .card-front .club-mark {
    position: absolute; left: 60px; top: 20px;
    display: flex; align-items: center; gap: 12px;
  }
  .card-front .mark-square { width: 34px; height: 34px; }
  .card-front .club-name {
    color: var(--ink); font-weight: 900; font-size: 32px;
  }
  .identity { position: absolute; left: 420px; top: 140px; }
  .role {
    color: #ffffff; font-weight: 700; font-size: 20px; letter-spacing: 3px;
  }
  .person-name {
    color: var(--club-blue); font-weight: 900; font-size: 30px;
    letter-spacing: 1.5px; text-transform: uppercase; margin-top: 2px;
  }
  .contact {
    position: absolute; left: 100px; top: 262px;
    color: var(--ink); font-size: 19px; line-height: 1.2; letter-spacing: 0.5px;
  }
  .contact .address { margin-bottom: 10px; }
  .contact li { list-style: none; display: flex; align-items: center; gap: 10px; margin-bottom: 2px; }
  .contact svg { width: 15px; height: 15px; fill: var(--club-blue); flex: none; }
  .ball {
    position: absolute; left: 330px; top: 300px; width: 560px; height: 560px;
    border-radius: 50%; background: var(--ball-grey);
  }
</style>
</head>
<body>

<section class="card card-back">
  <div class="club-mark">
    <span class="mark-square"></span>
    <span class="club-name">SC BRENVAL</span>
  </div>
</section>

<section class="card card-front">
  <div class="blue-band"></div>
  <div class="red-band"></div>
  <div class="ball" role="img" aria-label="Large football illustration"></div>

  <div class="club-mark">
    <span class="mark-square" style="background: var(--club-red);"></span>
    <span class="club-name">SC BRENVAL</span>
  </div>

  <div class="identity">
    <p class="role">President</p>
    <p class="person-name">Laurent Despratin</p>
  </div>

  <div class="contact">
    <p class="address">Rue du Stade 15<br>1873 Brenval</p>
    <ul>
      <li>
        <svg viewBox="0 0 24 24" aria-hidden="true"><path d="M6.6 10.8a15.1 15.1 0 0 0 6.6 6.6l2.2-2.2a1 1 0 0 1 1-.25 11.4 11.4 0 0 0 3.6.57 1 1 0 0 1 1 1V20a1 1 0 0 1-1 1A17 17 0 0 1 3 4a1 1 0 0 1 1-1h3.5a1 1 0 0 1 1 1c0 1.25.2 2.45.57 3.6a1 1 0 0 1-.25 1z"/></svg>
        41X-XXX-XXXX
      </li>
      <li>
        <svg viewBox="0 0 24 24" aria-hidden="true"><path d="M2 5h20v14H2z M4 7l8 6 8-6" fill="none" stroke="#1e8fd6" stroke-width="2"/></svg>
        first.lastname@scbrenval.ch
      </li>
      <li>
        <svg viewBox="0 0 24 24" aria-hidden="true"><circle cx="12" cy="12" r="10"/></svg>
        www.scbrenval.ch
      </li>
    </ul>
  </div>
</section>

</body>
</html>
```